Quarvella Brochure Design - IT Services - Modern Design - Services List

Hi,

We are looking for a modern IT Services brochure design of between 4 - 6 pages, it must be based on a blue and white colour theme with some nice technical imagery. It would need a section about why Quarvella and a contact section at the end.

Here is some info that could be included

Target Market(s)

Medium to Large Businesses

Industry/Entity Type

Information Technology

Colors
0054AA
0677BA
7BADD7
CADEEF
E8F1F8

Requirements
Must have
• Striking technical imagery
Nice to have
• Nice Icons to list the different services sections

```html
<!DOCTYPE html>
<html lang="en">
<head>
<meta charset="utf-8">
<title>Quarvella Brochure</title>
<link href="https://fonts.googleapis.com/css2?family=Poppins:wght@400;500;600;700;800&display=swap" rel="stylesheet">
<style>
:root{
  --navy:#0054AA;
  --blue:#0677BA;
  --sky:#1E95D6;
  --panel:#4A9FD6;
  --mist:#7BADD7;
  --ice:#CADEEF;
  --frost:#E8F1F8;
  --white:#ffffff;
  --stage:#6b6b6b;
  --ink:#1f2a36;
}
*{box-sizing:border-box;margin:0;padding:0}
html,body{width:1200px;height:2166px;overflow:hidden;background:var(--stage)}
body{font-family:'Poppins',sans-serif;color:var(--white);position:relative}
.page{position:absolute;width:498px;height:646px;overflow:hidden}
.p-cover{left:85px;top:69px}
.p-about{left:615px;top:69px;background:var(--sky)}
.p-managed{left:85px;top:761px;background:var(--white)}
.p-security{left:615px;top:761px;background:var(--white)}
.p-why{left:86px;top:1449px;background:var(--sky)}
.p-contact{left:615px;top:1452px;background:linear-gradient(160deg,#0a8fd4 0%,#0a86cc 50%,#0677BA 100%)}
.abs{position:absolute}
.fill{position:absolute;inset:0}
.shape{position:absolute;left:0;top:0}

/* brand */
.brand{position:absolute;font-weight:800;letter-spacing:.5px;line-height:1}
.brand small{display:block;font-weight:600;font-size:4.5px;letter-spacing:.3px;margin-top:2px;text-align:right}
.brand-white{color:var(--white);font-size:19px}
.brand-blue{color:var(--blue);font-size:19px}
.brand-blue small{color:var(--ink)}

/* page tabs */
.tab{position:absolute;right:0;bottom:26px;width:68px;height:22px;font-weight:800;font-size:13px;
  display:flex;align-items:center;justify-content:center;padding-left:10px;
  clip-path:polygon(14px 0,100% 0,100% 100%,0 100%)}
.tab-blue{background:var(--sky);color:var(--white)}
.tab-white{background:var(--white);color:var(--blue)}

/* cover */
.cover-logo{left:0;right:0;top:38px;text-align:center;color:var(--sky);font-size:44px;font-weight:800;letter-spacing:1px}
.cover-tag{left:230px;top:86px;color:var(--ink);font-size:11px;font-weight:600}
.cover-title{left:0;right:0;top:476px;text-align:center;font-size:24.5px;font-weight:800;line-height:29px}
.cover-web{left:0;right:0;top:587px;height:23px;background:var(--sky);text-align:center;font-size:11.5px;letter-spacing:8px;line-height:23px;font-weight:500}

/* headings */
.h-page{font-weight:800;font-size:21px;line-height:1}
.h-services{color:var(--sky);font-size:25px;font-weight:800;left:37px;top:30px}
.rule{position:absolute;height:2px;background:#8a96a3;width:58px}

/* service blocks */
.svc-icon{position:absolute;width:48px;height:48px;border-radius:50%;background:var(--white);border:2px solid var(--sky);display:flex;align-items:center;justify-content:center}
.svc-title{position:absolute;font-weight:800;font-size:12.5px}
.svc-lead{position:absolute;font-size:10.2px;line-height:13.8px;width:232px}
.item{position:absolute;font-size:8.2px;line-height:11.5px;width:104px}
.item b{font-weight:700;display:block}
.item::before{content:"";position:absolute;left:-14px;top:3px;width:6px;height:6px;border:1.2px solid var(--white);transform:rotate(45deg)}
.item.col2{width:100px}
.item.wide{width:215px}

/* why */
.why-lead{left:58px;top:65px;width:418px;font-size:8.7px;line-height:11.7px}
.feat-icon{position:absolute;width:49px;height:49px;border-radius:50%;border:1.5px solid var(--white);display:flex;align-items:center;justify-content:center}
.feat-title{position:absolute;font-weight:800;font-size:12.5px;line-height:15px}
.feat-body{position:absolute;width:186px;font-size:10.5px;line-height:13.8px}

/* contact */
.ct-title{left:0;right:0;top:190px;text-align:center;font-weight:800;font-size:31px}
.ct-rule{left:218px;top:244px;width:62px;height:2.5px;background:var(--white)}
.ct-lead{left:40px;right:40px;top:262px;text-align:center;font-size:11.3px;line-height:14.8px}
.ct-label{left:0;right:0;text-align:center;font-weight:700;font-size:13px;letter-spacing:4.5px}
.ct-line{left:0;right:0;text-align:center;font-size:11px}
.ct-row{left:50px;top:392px;display:flex;align-items:center;gap:8px;font-size:10.7px}
.ct-ico{width:26px;height:26px;border-radius:50%;border:1px solid var(--white);display:flex;align-items:center;justify-content:center}
.ct-gap{width:6px}
.socials{left:0;right:0;top:500px;display:flex;justify-content:center;gap:8px}
.social{width:22px;height:22px;border-radius:50%;background:var(--white)}
</style>
</head>
<body>

<!-- Cover -->
<section class="page p-cover">
  <div class="fill" style="background:linear-gradient(180deg,#1a9ad8 0%,#0a7fc4 70%,#0a72b6 100%)"></div>
  <svg class="shape" width="498" height="646" viewBox="0 0 498 646">
    <polygon points="0,0 498,0 498,88 250,160 0,88" fill="#f2f4f6"/>
    <polygon points="250,160 498,88 498,215" fill="#1E95D6"/>
  </svg>
  <div class="abs" role="img" aria-label="Hand touching a glowing digital data chart over a night city" style="left:0;top:0;width:498px;height:470px;background:linear-gradient(135deg,#0e3f6e 0%,#1b6aa3 35%,#0b2a4e 70%,#1a2f4a 100%);clip-path:polygon(0 89px,250px 160px,498px 225px,498px 470px,250px 392px,0 460px)"></div>
  <svg class="shape" width="498" height="646" viewBox="0 0 498 646">
    <polyline points="0,469 250,395 498,469" fill="none" stroke="#ffffff" stroke-width="8"/>
    <line x1="250" y1="160" x2="498" y2="235" stroke="#ffffff" stroke-width="1.5"/>
  </svg>
  <div class="abs cover-logo">Quarvella</div>
  <div class="abs cover-tag">COMPUTING EXCELLENCE</div>
  <h1 class="abs cover-title">EMPOWERING YOUR<br>BUSINESS WITH CUTTING-EDGE<br>IT SOLUTIONS</h1>
  <div class="abs cover-web">WWW.QUARVELLA.CO.UK</div>
</section>

<!-- About intro -->
<section class="page p-about">
  <div class="abs" role="img" aria-label="Businessman in a suit holding a tablet with glowing financial charts" style="left:0;top:0;width:498px;height:646px;background:linear-gradient(180deg,#1d3350 0%,#22324a 40%,#3a3520 65%,#12203a 100%)"></div>
  <svg class="shape" width="498" height="646" viewBox="0 0 498 646">
    <polygon points="0,0 498,0 498,150 250,226 0,150" fill="#1E95D6"/>
    <polyline points="0,122 110,158 0,178" fill="none" stroke="#ffffff" stroke-width="1.5"/>
    <polyline points="498,168 370,210 430,228" fill="none" stroke="#ffffff" stroke-width="1.5"/>
  </svg>
  <h2 class="abs h-page" style="left:45px;top:34px">ABOUT QUARVELLA</h2>
  <p class="abs" style="left:45px;top:63px;width:420px;font-size:8.7px;line-height:11.7px">At Quarvella, we are dedicated to providing top-tier IT services that drive efficiency, innovation, and growth for your business. With a commitment to excellence and a team of highly skilled professionals, we offer a comprehensive suite of solutions tailored to meet the unique needs of our clients.</p>
  <div class="brand brand-white" style="left:36px;top:597px">Quarvella<small>COMPUTING EXCELLENCE</small></div>
  <div class="tab tab-blue" style="bottom:24px">01</div>
</section>

<!-- Managed services -->
<section class="page p-managed">
  <div class="abs" role="img" aria-label="Hands typing on a laptop keyboard in soft light" style="left:0;top:0;width:498px;height:646px;background:linear-gradient(120deg,#ffffff 0%,#e6eaee 30%,#b9c2cb 55%,#8f9aa6 75%,#dfe4e9 100%)"></div>
  <svg class="shape" width="498" height="646" viewBox="0 0 498 646">
    <polygon points="209,93 498,0 498,646 209,646" fill="#4A9FD6"/>
    <polygon points="0,0 370,0 209,54 0,54" fill="#ffffff" opacity=".75"/>
  </svg>
  <h2 class="abs h-services">OUR SERVICES</h2>
  <div class="rule" style="left:39px;top:68px"></div>

  <div class="svc-icon" style="left:189px;top:116px"><svg width="26" height="26" viewBox="0 0 26 26" fill="none" stroke="#1E95D6" stroke-width="1.6"><rect x="3" y="5" width="20" height="13" rx="1"/><line x1="9" y1="22" x2="17" y2="22"/><line x1="13" y1="18" x2="13" y2="22"/><circle cx="13" cy="11.5" r="3"/></svg></div>
  <h3 class="svc-title" style="left:246px;top:120px">MANAGED IT SERVICES</h3>
  <p class="svc-lead" style="left:245px;top:139px">Our Managed IT Services provide proactive monitoring and management of your IT infrastructure, ensuring maximum uptime and reliability. We offer:</p>
  <div class="item" style="left:259px;top:210px"><b>24/7 Network Monitoring:</b>Continuous monitoring to detect and resolve issues before they impact your business.</div>
  <div class="item col2" style="left:385px;top:210px"><b>Patch Management:</b>Regular updates and patches to keep your systems secure and up-to-date.</div>
  <div class="item" style="left:259px;top:287px"><b>Helpdesk Support:</b>Responsive and knowledgeable support team available round the clock.</div>
  <div class="item col2" style="left:385px;top:282px"><b>IT Asset Management:</b>Comprehensive tracking and management of your IT assets</div>

  <div class="svc-icon" style="left:189px;top:370px"><svg width="26" height="26" viewBox="0 0 26 26" fill="none" stroke="#1E95D6" stroke-width="1.6"><path d="M7 18h12a4 4 0 0 0 0-8 6 6 0 0 0-11.5-1A4.5 4.5 0 0 0 7 18z"/><line x1="13" y1="12" x2="13" y2="23"/></svg></div>
  <h3 class="svc-title" style="left:246px;top:373px">CLOUD SOLUTIONS</h3>
  <p class="svc-lead" style="left:245px;top:392px">Embrace the power of the cloud with our scalable and secure cloud solutions. Our offerings include:</p>
  <div class="item" style="left:259px;top:452px"><b>Cloud Migration:</b>Seamless transition of your applications and data to the cloud.</div>
  <div class="item col2" style="left:385px;top:452px"><b>Backup and Disaster Recovery:</b>Robust backup and recovery solutions to ensure business continuity.</div>
  <div class="item" style="left:259px;top:511px"><b>Cloud Hosting:</b>Reliable and scalable hosting solutions to meet your growing needs.</div>
  <div class="item wide" style="left:259px;top:567px"><b>Software as a Service (SaaS):</b>Access to the latest software applications without the hassle of maintenance.</div>

  <div class="brand brand-blue" style="left:37px;top:598px">Quarvella<small>COMPUTING EXCELLENCE</small></div>
  <div class="tab tab-white">02</div>
</section>

<!-- Security & consulting -->
<section class="page p-security">
  <div class="abs" role="img" aria-label="Finger touching a glowing fingerprint scanner with security icons" style="left:0;top:0;width:498px;height:646px;background:radial-gradient(circle at 70px 190px,#bfe9ee 0%,#e9edf0 25%,#f3f3f3 45%,#e8c7ae 70%,#f4f4f4 100%)"></div>
  <svg class="shape" width="498" height="646" viewBox="0 0 498 646">
    <polygon points="209,93 498,0 498,646 209,646" fill="#4A9FD6"/>
    <polygon points="0,0 370,0 209,54 0,54" fill="#ffffff" opacity=".8"/>
  </svg>
  <h2 class="abs h-services">OUR SERVICES</h2>
  <div class="rule" style="left:39px;top:68px"></div>

  <div class="svc-icon" style="left:190px;top:116px"><svg width="26" height="26" viewBox="0 0 26 26" fill="none" stroke="#1E95D6" stroke-width="1.6"><rect x="8" y="12" width="10" height="9" rx="1"/><path d="M10 12V9a3 3 0 0 1 6 0v3"/><circle cx="13" cy="13" r="11"/></svg></div>
  <h3 class="svc-title" style="left:246px;top:120px">CYBER SECURITY</h3>
  <p class="svc-lead" style="left:245px;top:139px">Protect your business from evolving threats with our comprehensive cybersecurity services. We offer:</p>
  <div class="item" style="left:259px;top:197px"><b>Threat Detection and Response:</b>Advanced threat monitoring and response to safeguard your data.</div>
  <div class="item col2" style="left:385px;top:197px"><b>Endpoint Protection:</b>Robust security solutions for all your devices.</div>
  <div class="item" style="left:259px;top:269px"><b>Security Audits and Assessments:</b>Thorough evaluations to identify and mitigate vulnerabilities.</div>
  <div class="item col2" style="left:385px;top:257px"><b>Compliance and Regulatory Services:</b>Ensure adherence to industry standards and regulations.</div>

  <div class="svc-icon" style="left:190px;top:350px"><svg width="26" height="26" viewBox="0 0 26 26" fill="none" stroke="#1E95D6" stroke-width="1.6"><path d="M5 14a8 8 0 0 1 16 0"/><rect x="3" y="14" width="4" height="6" rx="1"/><rect x="19" y="14" width="4" height="6" rx="1"/><rect x="9" y="11" width="8" height="6" rx="1"/></svg></div>
  <h3 class="svc-title" style="left:246px;top:353px">IT CONSULTING</h3>
  <p class="svc-lead" style="left:245px;top:372px">Leverage our expertise to drive your IT strategy and achieve your business goals. Our consulting services include:</p>
  <div class="item" style="left:259px;top:431px"><b>IT Strategy and Planning:</b>Strategic guidance to align your IT initiatives with your business objectives.</div>
  <div class="item col2" style="left:385px;top:431px"><b>Business Continuity Planning:</b>Strategies to ensure your business remains operational during disruptions.</div>
  <div class="item" style="left:259px;top:514px"><b>Technology Assessments:</b>In-depth evaluations to optimize your IT infrastructure.</div>
  <div class="item wide" style="left:259px;top:572px"><b>Project Management:</b>Expert management of IT projects from inception to completion.</div>

  <div class="brand brand-blue" style="left:37px;top:600px">Quarvella<small>COMPUTING EXCELLENCE</small></div>
  <div class="tab tab-white">03</div>
</section>

<!-- Why Quarvella -->
<section class="page p-why" style="width:502px;height:649px">
  <h2 class="abs h-page" style="left:58px;top:33px">ABOUT QUARVELLA</h2>
  <p class="abs why-lead">At Quarvella, we are dedicated to providing top-tier IT services that drive efficiency, innovation, and growth for your business. With a commitment to excellence and a team of highly skilled professionals, we offer a comprehensive suite of solutions tailored to meet the unique needs of our clients.</p>

  <div class="feat-icon" style="left:43px;top:130px"><svg width="28" height="28" viewBox="0 0 28 28" fill="none" stroke="#fff" stroke-width="1.5"><circle cx="12" cy="12" r="5"/><circle cx="12" cy="12" r="9" stroke-dasharray="3 2.5"/><path d="M17 20l3 3 6-6"/></svg></div>
  <h3 class="feat-title" style="left:101px;top:138px">EXPERTISE<br>AND EXPERIENCE</h3>
  <p class="feat-body" style="left:47px;top:187px">With years of experience in the IT industry, our team possesses the knowledge and skills to tackle any challenge. We stay abreast of the latest technological advancements to provide you with cutting-edge solutions.</p>

  <div class="feat-icon" style="left:266px;top:130px"><svg width="28" height="28" viewBox="0 0 28 28" fill="none" stroke="#fff" stroke-width="1.5"><circle cx="8" cy="7" r="2.5"/><circle cx="14" cy="6" r="2.5"/><circle cx="20" cy="7" r="2.5"/><path d="M4 20l6-5h8l6 5"/><path d="M10 19l4 3 4-3"/></svg></div>
  <h3 class="feat-title" style="left:324px;top:138px">CUSTOMER-CENTRIC<br>APPROACH</h3>
  <p class="feat-body" style="left:270px;top:187px">We prioritize our clients' needs and work closely with them to deliver customized solutions that drive success. Our client-centric approach ensures that we are always aligned with your business goals.</p>

  <div class="feat-icon" style="left:43px;top:299px"><svg width="28" height="28" viewBox="0 0 28 28" fill="none" stroke="#fff" stroke-width="1.5"><path d="M5 17l6-6 4 4 8-8"/><path d="M17 7h6v6"/><line x1="4" y1="23" x2="24" y2="23"/></svg></div>
  <h3 class="feat-title" style="left:101px;top:307px">PROACTIVE<br>SUPPORT</h3>
  <p class="feat-body" style="left:47px;top:357px">Our proactive support model ensures that potential issues are identified and resolved before they can impact your operations. We are committed to maintaining the highest levels of service availability and performance.</p>

  <div class="feat-icon" style="left:266px;top:299px"><svg width="28" height="28" viewBox="0 0 28 28" fill="none" stroke="#fff" stroke-width="1.5"><rect x="5" y="5" width="8" height="8"/><rect x="15" y="5" width="8" height="8"/><rect x="5" y="15" width="8" height="8"/><rect x="15" y="15" width="8" height="8"/></svg></div>
  <h3 class="feat-title" style="left:324px;top:307px">COMPREHENSIVE<br>SOLUTIONS</h3>
  <p class="feat-body" style="left:270px;top:357px;width:210px">From managed services to cybersecurity, we offer a comprehensive suite of IT solutions designed to meet the diverse needs of your business. Our holistic approach ensures that all aspects of your IT infrastructure are covered.</p>

  <div class="abs" role="img" aria-label="Programmer typing code on a laptop with code overlay" style="left:0;top:0;width:502px;height:649px;background:linear-gradient(160deg,#2a3a4c 0%,#4a5868 45%,#1e2a38 100%);clip-path:polygon(0 472px,250px 542px,502px 472px,502px 649px,0 649px)"></div>
  <svg class="shape" width="502" height="649" viewBox="0 0 502 649">
    <polyline points="0,472 250,542 502,472" fill="none" stroke="#ffffff" stroke-width="6"/>
    <polyline points="502,482 310,530 360,543" fill="none" stroke="#ffffff" stroke-width="1.5"/>
  </svg>
  <div class="brand brand-white" style="left:37px;top:598px">Quarvella<small>COMPUTING EXCELLENCE</small></div>
  <div class="tab tab-blue" style="bottom:24px">04</div>
</section>

<!-- Contact -->
<section class="page p-contact">
  <h2 class="abs ct-title">GET IN TOUCH</h2>
  <div class="abs ct-rule"></div>
  <p class="abs ct-lead">Discover how Quarvella can transform your IT landscape and drive your business forward. Contact us today to learn more about our services and how we can help you achieve your goals.</p>
  <div class="abs ct-label" style="top:343px">CONTACT US</div>
  <div class="abs ct-line" style="top:371px">Upper Ashford Lodge, Fernbrook Lane, Northwell, NW4 2QT</div>
  <div class="abs ct-row">
    <span class="ct-ico"><svg width="14" height="14" viewBox="0 0 14 14" fill="none" stroke="#fff" stroke-width="1"><circle cx="7" cy="7" r="6"/><ellipse cx="7" cy="7" rx="2.6" ry="6"/><line x1="1" y1="7" x2="13" y2="7"/></svg></span>
    <span>www.quarvella.co.uk</span><span class="ct-gap"></span>
    <span class="ct-ico"><svg width="14" height="14" viewBox="0 0 14 14" fill="#fff"><path d="M3 1.5l2.2 0 1 3-1.4 1a7 7 0 0 0 3.7 3.7l1-1.4 3 1v2.2a1.3 1.3 0 0 1-1.4 1.3A10.5 10.5 0 0 1 1.7 2.9 1.3 1.3 0 0 1 3 1.5z"/></svg></span>
    <span>01632 960482</span><span class="ct-gap"></span>
    <span class="ct-ico"><svg width="14" height="14" viewBox="0 0 14 14" fill="none" stroke="#fff" stroke-width="1"><rect x="1.5" y="3" width="11" height="8"/><polyline points="1.5,3 7,8 12.5,3"/></svg></span>
    <span>info@quarvella.co.uk</span>
  </div>
  <div class="abs ct-label" style="top:458px">FOLLOW US</div>
  <div class="abs ct-line" style="top:482px">Stay updated with the latest news and updates from Quarvella</div>
  <div class="abs socials"><span class="social"></span><span class="social"></span><span class="social"></span></div>
</section>

</body>
</html>
```